Building and Construction Business Card Design

We need a business card design for a new building and construction company called "Harbourline Estates Pty Ltd" We will build any type of building, but our main focus is luxury homes in Sydney.
We would like our business card to be elegant and strong. We have played around with colours and like greys/black and red, but are open to pretty open minded.
Updates

Project Deadline Extended
Reason: Designs are either plain without any wow, or a little comical. Hopefully we can get some designs that are more eye catching, maybe some bling (silver/ gold script) something different please. Thank you for your submissions so far.

Target Market(s)

high end real estate market

Industry/Entity Type

Construction

Contact Information for Business Card

Teodor Halloran
Director/Fully Licenced Builder
ABN: 72504918337
m: 0491 573 812
e: info@harbourlineestates.com.au
HARBOURLINE ESTATES
website: www.harbourlineestates.com.au

Building and Construction

Colors

Designer to choose colors to be used in the design.

Requirements
Nice to have
• The business name "Harbourline Estates" on one side then all the info on the otherside.

```html
<!DOCTYPE html>
<html lang="en">
<head>
<meta charset="utf-8">
<title>Harbourline Estates – Business Card</title>
<link rel="stylesheet" href="https://fonts.googleapis.com/css2?family=Russo+One&family=Ubuntu:wght@500;700&display=swap">
<style>
  :root {
    --bg: #d9d9d9;
    --card-dark: #3a3a3a;
    --card-light: #f4f4f4;
    --ink: #2b2b2b;
    --ink-muted: #8a8a8a;
    --stripe: #9a9a9a;
    --white: #ffffff;
  }
  * { box-sizing: border-box; margin: 0; padding: 0; }
  html, body {
    width: 1200px;
    height: 800px;
    overflow: hidden;
  }
  body {
    background: radial-gradient(ellipse at 50% 20%, #ececec 0%, var(--bg) 70%);
    display: flex;
    align-items: center;
    justify-content: center;
    gap: 60px;
  }
  .card {
    position: relative;
    width: 520px;
    height: 318px;
    overflow: hidden;
    box-shadow: 0 10px 24px rgba(0,0,0,0.18);
  }

  /* Brand side */
  .card--brand {
    background: var(--card-dark);
    display: flex;
    align-items: center;
    justify-content: center;
    gap: 22px;
  }
  .brand-name {
    font-family: "Russo One", sans-serif;
    font-weight: 400;
    color: var(--white);
    font-size: 44px;
    line-height: 1.05;
    letter-spacing: 1px;
  }
  .brand-mark {
    width: 26px;
    height: 26px;
    background: var(--white);
  }

  /* Contact side */
  .card--contact { background: var(--card-light); }
  .card__swoosh {
    position: absolute;
    inset: 0;
    width: 100%;
    height: 100%;
  }
  .contact {
    position: relative;
    z-index: 1;
    padding: 56px 0 0 38px;
    font-family: "Ubuntu", sans-serif;
    font-weight: 700;
    color: var(--ink);
  }
  .contact__name {
    font-family: "Russo One", sans-serif;
    font-weight: 400;
    font-size: 21px;
    line-height: 1.2;
    letter-spacing: 0.5px;
    text-transform: uppercase;
  }
  .contact__role {
    font-size: 15px;
    line-height: 1.3;
    color: var(--ink-muted);
    margin-top: 2px;
  }
  .contact__abn {
    font-size: 14px;
    line-height: 1.3;
    margin-top: 18px;
  }
  .label {
    color: var(--ink-muted);
    display: inline-block;
    width: 26px;
  }
  .contact__abn .label { width: auto; margin-right: 8px; }
  .contact__list {
    list-style: none;
    margin-top: 26px;
    font-size: 14px;
    line-height: 1.35;
  }
</style>
</head>
<body>
  <section class="card card--brand" aria-label="Business card front">
    <p class="brand-name">HARBOURLINE<br>ESTATES</p>
    <span class="brand-mark" aria-hidden="true"></span>
  </section>

  <section class="card card--contact" aria-label="Business card back">
    <svg class="card__swoosh" viewBox="0 0 520 318" preserveAspectRatio="none" aria-hidden="true">
      <path d="M0,282 C200,282 400,236 520,154 L520,170 C400,252 200,298 0,298 Z" fill="var(--stripe)"/>
      <path d="M0,298 C200,298 400,252 520,170 L520,318 L0,318 Z" fill="var(--card-dark)"/>
    </svg>
    <div class="contact">
      <h1 class="contact__name">Teodor Halloran</h1>
      <p class="contact__role">Director/Fully Licenced Builder</p>
      <p class="contact__abn"><span class="label">ABN:</span>72504918337</p>
      <ul class="contact__list">
        <li><span class="label">E:</span>info@harbourlineestates.com.au</li>
        <li><span class="label">P:</span>0491 573 812</li>
        <li><span class="label">W:</span>www.harbourlineestates.com.au</li>
      </ul>
    </div>
  </section>
</body>
</html>
```